Property Management Company Business Cards

Need business cards for a property management company located in Michigan. We manage houses for clients all over the world. Young and modern company, looking for eye catching design. Please work with the attached logo.

Industry/Entity Type

Property Management

Requirements
Must have
• Need lines for address, telephone number, fax number, web site.

Also lines for name, and job title

```html
<!DOCTYPE html>
<html lang="en">
<head>
<meta charset="utf-8">
<title>Lakeshore Harbor Management – Business Card</title>
<link rel="stylesheet" href="https://fonts.googleapis.com/css2?family=Source+Sans+3:wght@400;700&display=swap">
<style>
  :root {
    --brand-blue: #0ba1dd;
    --ink: #1f1f1f;
    --paper: #ffffff;
    --backdrop: #ffffff;
    --card-shadow: 0 2px 6px rgba(0, 0, 0, 0.35);
  }
  * { margin: 0; padding: 0; box-sizing: border-box; }
  html, body {
    width: 1200px;
    height: 1000px;
    overflow: hidden;
    background: var(--backdrop);
    font-family: "Source Sans 3", sans-serif;
  }
  .canvas {
    position: relative;
    width: 1200px;
    height: 1000px;
  }
  .card {
    position: absolute;
    left: 311px;
    width: 576px;
    height: 359px;
    box-shadow: var(--card-shadow);
  }
  .card--front {
    top: 133px;
    background: var(--brand-blue);
    display: flex;
    align-items: center;
    justify-content: center;
  }
  .card--back {
    top: 506px;
    background: var(--paper);
  }
  .front-name {
    color: var(--paper);
    font-weight: 700;
    font-size: 30px;
    letter-spacing: 0.5px;
    text-align: center;
    line-height: 1.15;
    text-transform: uppercase;
  }
  .brand {
    position: absolute;
    left: 42px;
    top: 36px;
    display: flex;
    align-items: center;
    gap: 14px;
  }
  .brand__dot {
    width: 64px;
    height: 64px;
    border-radius: 50%;
    background: var(--brand-blue);
    flex: none;
  }
  .brand__name {
    color: var(--ink);
    font-weight: 700;
    font-size: 25px;
    line-height: 1.1;
    text-transform: uppercase;
    letter-spacing: -0.2px;
  }
  .holder {
    position: absolute;
    left: 44px;
    top: 150px;
  }
  .holder__name {
    color: var(--ink);
    font-weight: 700;
    font-size: 21px;
    line-height: 26px;
  }
  .holder__title {
    color: var(--brand-blue);
    font-weight: 400;
    font-size: 16.5px;
    line-height: 22px;
  }
  .contact {
    position: absolute;
    top: 261px;
    font-size: 16.5px;
    line-height: 21.5px;
    color: var(--ink);
  }
  .contact--lines { left: 40px; }
  .contact--address { left: 318px; }
  .contact__row {
    display: flex;
  }
  .contact__label {
    width: 24px;
    text-align: center;
    color: var(--brand-blue);
    font-weight: 700;
    margin-right: 16px;
  }
  .contact--address .contact__label { margin-right: 12px; }
</style>
</head>
<body>
  <main class="canvas">
    <section class="card card--front" aria-label="Card front">
      <p class="front-name">Lakeshore Harbor<br>Management</p>
    </section>

    <section class="card card--back" aria-label="Card back">
      <div class="brand">
        <span class="brand__dot" aria-hidden="true"></span>
        <p class="brand__name">Lakeshore Harbor<br>Management</p>
      </div>

      <div class="holder">
        <p class="holder__name">Jordan Ellis</p>
        <p class="holder__title">Property Manager</p>
      </div>

      <div class="contact contact--lines">
        <div class="contact__row"><span class="contact__label">T</span><span>555 201 3847</span></div>
        <div class="contact__row"><span class="contact__label">F</span><span>555 201 3849</span></div>
        <div class="contact__row"><span class="contact__label">W</span><span>www.lakeshoreharbor.com</span></div>
      </div>

      <div class="contact contact--address">
        <div class="contact__row"><span class="contact__label">A</span><span>4471 Maple Row<br>Fairhaven, Michigan<br>48099</span></div>
      </div>
    </section>
  </main>
</body>
</html>
```